Orlow Wellness Group Website

Need a informative, detailed and functional website for a medical cannabis clinic website

check out www.tesmorahealthcare.com as competition - want better site than they have

Target Market(s)

Patients

Industry/Entity Type

Health Care

Number of Pages Required

1 page

Font styles to use
Sans Serif

Colors
cadf82
abd036
9bcb3b
3276b5
33a6d7
0392cd
f68d4e

Requirements
Must have
• Clean / Informative
• Will add additional educational content on opioid reduction
Nice to have
• like the white contrast with black/slate dividers. Green logo looks good on slate
• Check documents for ppt regarding website ideas
Should not have
• too many words

```html
<!DOCTYPE html>
<html lang="en">
<head>
<meta charset="utf-8">
<title>Orlow Wellness Group</title>
<link href="https://fonts.googleapis.com/css2?family=Montserrat:wght@400;500;600;700&family=Open+Sans:wght@400;600&display=swap" rel="stylesheet">
<style>
:root{
  --green:#9bcb3b;
  --green-light:#abd036;
  --green-pale:#cadf82;
  --ink:#1a1a1a;
  --slate:#161616;
  --grey:#f2f2f2;
  --text:#444;
  --muted:#777;
  --white:#fff;
}
*{box-sizing:border-box;margin:0;padding:0}
html,body{width:1200px;height:4248px;overflow:hidden}
body{font-family:"Open Sans",sans-serif;color:var(--text);background:var(--white);position:relative}
h1,h2,h3,h4,.head{font-family:"Montserrat",sans-serif;color:var(--ink)}
.container{position:absolute;left:148px;width:904px}

/* top bar */
.topbar{position:absolute;top:0;left:0;width:1200px;height:36px;background:var(--green);color:#fff;font-size:12px}
.topbar .contact{position:absolute;left:162px;top:10px;display:flex;gap:26px}
.topbar .social{position:absolute;right:150px;top:10px;display:flex;gap:14px}
.dot{width:14px;height:14px;border-radius:50%;background:#fff;display:block}

/* nav */
.nav{position:absolute;top:36px;left:0;width:1200px;height:110px;background:#fff}
.brand{position:absolute;left:162px;top:36px;display:flex;align-items:center;gap:12px}
.brand-mark{width:30px;height:30px;border-radius:50%;background:var(--green)}
.brand-name{font-family:"Montserrat",sans-serif;font-weight:600;font-size:15px;color:var(--green);letter-spacing:1px;text-transform:uppercase;line-height:1.2;width:130px}
.menu{position:absolute;left:0;top:52px;width:1200px;font-family:"Montserrat",sans-serif;font-size:12px;color:#333}
.menu span{position:absolute;white-space:nowrap}
.search{position:absolute;left:1022px;top:42px;width:30px;height:30px;border:2px solid #333;border-radius:50%}

/* hero */
.hero{position:absolute;top:146px;left:0;width:1200px;height:628px;background:linear-gradient(110deg,#3c3a20 0%,#a8752c 30%,#d99b45 45%,#6f6a3a 70%,#2f3a1c 100%)}
.hero .eyebrow{position:absolute;left:185px;top:180px;color:#fff;font-family:"Montserrat",sans-serif;font-size:14px;letter-spacing:1px}
.hero h1{position:absolute;left:185px;top:210px;color:#fff;font-size:40px;font-weight:700;letter-spacing:1px}
.hero p{position:absolute;left:185px;top:280px;width:420px;color:#fff;font-size:14px;line-height:1.6}
.btn{display:inline-block;background:var(--green);color:#fff;font-family:"Montserrat",sans-serif;font-size:14px;border-radius:26px;text-align:center}
.hero .btn{position:absolute;left:185px;top:348px;width:180px;height:46px;line-height:46px;border:3px solid rgba(255,255,255,.35)}

/* process cards */
.steps-cards{top:825px;height:313px;display:flex}
.pcard{flex:1;background:var(--grey);text-align:center;padding-top:42px;position:relative}
.pcard.active{background:var(--green)}
.pcard h3{font-size:18px;font-weight:700;margin-bottom:28px}
.pcard.active h3,.pcard.active p{color:#fff}
.pcard .ic{width:84px;height:84px;border-radius:50%;background:var(--green);margin:0 auto 26px;display:flex;align-items:center;justify-content:center;border:4px solid #e3efc6}
.pcard.active .ic{background:#fff;border-color:rgba(255,255,255,.5)}
.pcard p{font-size:13px;line-height:1.6;width:230px;margin:0 auto;color:var(--text)}
.arrow{position:absolute;top:135px;z-index:2}

/* section divider */
.divider{position:absolute;left:0;width:1200px;display:flex;justify-content:center;align-items:center;gap:14px}
.divider span{width:70px;height:1px;background:#ccc}
.divider i{width:22px;height:22px;border-radius:50%;background:var(--green);display:block}
.divider.dark span{background:#444}

/* network */
.network h2{position:absolute;top:1252px;width:1200px;left:0;text-align:center;font-size:34px;font-weight:700;letter-spacing:1px}
.network h2 em{font-style:normal;font-weight:400;color:var(--green)}
.network p{position:absolute;top:1320px;left:226px;width:748px;text-align:center;font-size:13px;line-height:2}
.network .btn{position:absolute;top:1473px;left:519px;width:162px;height:52px;line-height:52px}

/* dark steps */
.process{position:absolute;top:1587px;left:0;width:1200px;height:728px;background:var(--slate);color:#ddd}
.process h2{position:absolute;top:130px;width:1200px;text-align:center;color:#fff;font-size:24px;font-weight:700}
.process .intro{position:absolute;top:175px;left:260px;width:680px;text-align:center;font-size:13px;line-height:2.1}
.track{position:absolute;top:367px;left:360px;width:480px;height:1px;background:#444}
.step{position:absolute;top:270px;width:300px;text-align:center}
.step .circle{position:relative;width:194px;height:194px;margin:0 auto;border-radius:50%;background:var(--green);border:10px solid #fff;display:flex;align-items:center;justify-content:center}
.step .badge{position:absolute;right:-14px;top:-4px;width:46px;height:46px;border-radius:50%;background:#2a2a2a;display:flex;align-items:center;justify-content:center}
.step h4{color:#fff;font-size:16px;font-weight:700;line-height:1.9;margin-top:46px}
.step p{font-size:13px;line-height:1.75;margin-top:28px;padding:0 16px}

/* benefits */
.benefit-photo{position:absolute;left:142px;top:2432px;width:378px;height:426px;border:4px solid var(--green);padding:10px;background:#fff}
.benefit-photo div{width:100%;height:100%;background:radial-gradient(circle at 70% 30%,#f1c24d 0%,#c58a24 35%,#6f7a24 70%,#3d4a16 100%)}
.benefits .eyebrow{position:absolute;left:574px;top:2394px;font-family:"Montserrat",sans-serif;font-size:14px;letter-spacing:1px;color:#333}
.benefits h2{position:absolute;left:574px;top:2420px;font-size:32px;font-weight:600}
.bitem{position:absolute;width:220px}
.bitem .ic{width:54px;height:54px;border-radius:50%;background:var(--green);border:4px solid #e3efc6;display:flex;align-items:center;justify-content:center}
.bitem h4{font-size:15px;font-weight:700;margin:20px 0 12px}
.bitem p{font-size:12px;line-height:1.8}

/* doctor banner */
.banner{position:absolute;top:2935px;left:0;width:1200px;height:284px;background:linear-gradient(180deg,#23301d 0%,#3a4a2c 50%,#1f2818 100%)}
.banner h2{position:absolute;top:108px;width:1200px;text-align:center;color:#fff;font-size:32px;font-weight:700;letter-spacing:1px}
.banner .btn{position:absolute;top:183px;left:532px;width:136px;height:42px;line-height:42px;font-size:12px}

/* network cards */
.local h2{position:absolute;top:3336px;width:1200px;text-align:center;font-size:24px;font-weight:700}
.local .intro{position:absolute;top:3384px;left:220px;width:760px;text-align:center;font-size:13px;line-height:2.1}
.fcard{position:absolute;top:3484px;width:288px;height:318px;background:var(--grey)}
.fcard .ph{height:166px;background:linear-gradient(135deg,#2f6a1e,#6fa83a 55%,#b3d46a)}
.fcard h4{text-align:center;font-size:15px;font-weight:700;margin:30px 0 16px}
.fcard p{text-align:center;font-size:13px;line-height:1.6;padding:0 34px}

/* footer */
.footer{position:absolute;top:3859px;left:0;width:1200px;height:370px;background:#3b3d3a;color:#e5e5e5}
.footer .brand{left:148px;top:54px}
.footer .brand-name{color:#fff}
.footer .about{position:absolute;left:148px;top:140px;width:240px;font-size:12px;line-height:1.7}
.footer h4{position:absolute;top:62px;color:#fff;font-size:17px;font-weight:700}
.links{position:absolute;left:412px;top:106px;list-style:none;font-size:12px;line-height:2.1}
.links li::before{content:"› ";color:var(--green)}
.clist{position:absolute;left:552px;top:106px;list-style:none;font-size:12px}
.clist li{display:flex;align-items:center;gap:12px;height:48px}
.form{position:absolute;left:784px;top:108px;width:276px}
.form .row{display:flex;gap:6px;margin-bottom:8px}
.field{background:#6a6c69;height:32px;color:#ddd;font-size:11px;padding:9px 8px;flex:1}
.field.msg{height:96px}
.form .btn{width:92px;height:30px;line-height:30px;font-size:12px;margin-top:10px}
.copy{position:absolute;top:4229px;left:0;width:1200px;height:19px;background:#fff}
.copy p{position:absolute;left:148px;top:2px;font-size:11px;color:#555}
.copy .social{position:absolute;right:148px;top:-4px;display:flex;gap:10px}
.copy .dot{width:22px;height:22px;background:var(--green)}
</style>
</head>
<body>

<div class="topbar">
  <div class="contact"><span>☎ 00-555-0142</span><span>✉ hello@orlowwellness.com</span></div>
  <div class="social"><i class="dot"></i><i class="dot"></i><i class="dot"></i></div>
</div>

<header class="nav">
  <div class="brand" style="top:26px"><i class="brand-mark"></i><span class="brand-name">Orlow Wellness Group</span></div>
  <nav class="menu">
    <span style="left:432px">Home</span>
    <span style="left:510px">About</span>
    <span style="left:590px">Qualify</span>
    <span style="left:680px">Appointments</span>
    <span style="left:808px">FAQ</span>
    <span style="left:876px">News</span>
    <span style="left:948px">Contact</span>
  </nav>
  <span class="search"></span>
</header>

<section class="hero" role="img" aria-label="Woman with open arms in a green field at sunset">
  <div class="eyebrow">WE HELP CANNABIS</div>
  <h1>ARKANSAS MEDICAL</h1>
  <p>Licensed physicians help qualifying patients find relief and secure their state card.</p>
  <span class="btn">Book Appointment</span>
</section>

<section class="container steps-cards">
  <div class="pcard active">
    <h3>Meet a Arkansas Doctor</h3>
    <div class="ic"><svg width="34" height="34" viewBox="0 0 34 34" fill="none" stroke="#9bcb3b" stroke-width="2.5"><circle cx="17" cy="11" r="6"/><path d="M5 31c0-7 5-11 12-11s12 4 12 11"/></svg></div>
    <p>See a certified physician who reviews your records and condition.</p>
  </div>
  <div class="pcard">
    <h3>Apply for Arkansas Card</h3>
    <div class="ic"><svg width="30" height="34" viewBox="0 0 30 34" fill="none" stroke="#fff" stroke-width="2.5"><rect x="3" y="2" width="24" height="30" rx="2"/><path d="M9 11h12M9 17h12M9 23h8"/></svg></div>
    <p>We file your state paperwork so your card arrives quickly.</p>
  </div>
  <div class="pcard">
    <h3>Follow-up Appointment</h3>
    <div class="ic"><svg width="34" height="34" viewBox="0 0 34 34" fill="none" stroke="#fff" stroke-width="2.5"><circle cx="17" cy="17" r="14"/><path d="M17 9v9l6 4"/></svg></div>
    <p>Return visits keep your treatment plan safe and on track.</p>
  </div>
  <svg class="arrow" style="left:236px" width="70" height="30" viewBox="0 0 70 30" fill="none" stroke="#555" stroke-width="2"><path d="M2 24C20 2 46 2 64 18"/><path d="M56 18h8v-8"/></svg>
  <svg class="arrow" style="left:538px" width="70" height="30" viewBox="0 0 70 30" fill="none" stroke="#555" stroke-width="2"><path d="M2 24C20 2 46 2 64 18"/><path d="M56 18h8v-8"/></svg>
</section>

<div class="divider" style="top:1206px"><span></span><i></i><span></span></div>
<section class="network">
  <h2>ARKANSAS <em>ORLOW WELLNESS GROUP</em></h2>
  <p>Our clinic connects Arkansas patients with caring physicians who understand medical cannabis. We review your history, explain the qualifying conditions and help you build a plan that may reduce reliance on opioids. Every visit is private, respectful and focused on your long term health. Our team answers questions about dosing, safety and state rules so you can move forward with confidence and clear next steps from the very first call.</p>
  <span class="btn">More Info</span>
</section>

<section class="process">
  <div class="divider dark" style="top:80px"><span></span><i></i><span></span></div>
  <h2>Application &amp; Approval - In 3 Easy Steps</h2>
  <p class="intro">Getting started is simple. Apply online, meet a physician and receive your recommendation, often in a single week.</p>
  <div class="track"></div>
  <div class="step" style="left:150px">
    <div class="circle"><span class="badge"><svg width="16" height="16" viewBox="0 0 16 16" fill="none" stroke="#fff" stroke-width="2"><path d="M8 2v11M3 8l5 5 5-5"/></svg></span>
      <svg width="70" height="74" viewBox="0 0 70 74" fill="none" stroke="#fff" stroke-width="3"><rect x="6" y="4" width="40" height="56" rx="3"/><rect x="22" y="14" width="40" height="56" rx="3" fill="#9bcb3b"/><path d="M30 28h24M30 38h24M30 48h16"/></svg></div>
    <h4>Complete Your application<br>Here Online</h4>
    <p>Fill out a short secure form with your details and medical history in minutes.</p>
  </div>
  <div class="step" style="left:450px">
    <div class="circle"><span class="badge"><svg width="16" height="16" viewBox="0 0 16 16" fill="none" stroke="#fff" stroke-width="2"><path d="M8 2v11M3 8l5 5 5-5"/></svg></span>
      <svg width="70" height="74" viewBox="0 0 70 74" fill="none" stroke="#fff" stroke-width="3"><circle cx="35" cy="22" r="14"/><path d="M8 72c0-16 12-26 27-26s27 10 27 26"/><path d="M30 56h10M35 51v10"/></svg></div>
    <h4>Get a Doctor's<br>Recommendation</h4>
    <p>A licensed physician reviews your case and writes a recommendation if you qualify.</p>
  </div>
  <div class="step" style="left:750px">
    <div class="circle"><span class="badge"><svg width="16" height="16" viewBox="0 0 16 16" fill="none" stroke="#fff" stroke-width="2"><path d="M8 2v11M3 8l5 5 5-5"/></svg></span>
      <svg width="76" height="64" viewBox="0 0 76 64" fill="none" stroke="#fff" stroke-width="3"><rect x="4" y="14" width="68" height="46" rx="4"/><path d="M26 14V6h24v8"/><path d="M38 26v22M27 37h22"/></svg></div>
    <h4>Getting Medical<br>Marijuana</h4>
    <p>Register with the state and visit a licensed dispensary with your new card.</p>
  </div>
</section>

<section class="benefits">
  <div class="benefit-photo"><div role="img" aria-label="Cannabis plant glowing in golden sunlight"></div></div>
  <div class="eyebrow">BENEFITS YOU GET WITH</div>
  <h2>Arkansas Medical Cannabis</h2>
  <div class="bitem" style="left:568px;top:2508px"><div class="ic"><svg width="22" height="22" viewBox="0 0 22 22" fill="none" stroke="#fff" stroke-width="2"><circle cx="11" cy="7" r="4"/><path d="M3 21c0-5 4-8 8-8s8 3 8 8"/></svg></div><h4>Meet a Arkansa Doctor</h4><p>A physician visit focused on your condition and goals.</p></div>
  <div class="bitem" style="left:822px;top:2508px"><div class="ic"><svg width="20" height="22" viewBox="0 0 20 22" fill="none" stroke="#fff" stroke-width="2"><rect x="2" y="1" width="16" height="20" rx="1"/><path d="M6 7h8M6 12h8M6 16h5"/></svg></div><h4>Apply For Card</h4><p>We prepare and submit your state card application.</p></div>
  <div class="bitem" style="left:568px;top:2680px"><div class="ic"><svg width="22" height="22" viewBox="0 0 22 22" fill="none" stroke="#fff" stroke-width="2"><circle cx="11" cy="11" r="9"/><path d="M11 6v6l4 2"/></svg></div><h4>Follow Up Appointment</h4><p>Check-ins to adjust your plan as your needs change.</p></div>
  <div class="bitem" style="left:822px;top:2680px"><div class="ic"><svg width="22" height="22" viewBox="0 0 22 22" fill="none" stroke="#fff" stroke-width="2.4"><path d="M4 11l5 5 9-10"/></svg></div><h4>Lorem Ipsum</h4><p>Guidance on safe use and reducing opioid reliance.</p></div>
</section>

<section class="banner" role="img" aria-label="Dark background of cannabis leaves">
  <div class="divider dark" style="top:58px"><span></span><i></i><span></span></div>
  <h2>MEET OUR ARKANSAS MEDICAL DOCTOR</h2>
  <span class="btn">Book Appointment</span>
</section>

<section class="local">
  <div class="divider" style="top:3278px"><span></span><i></i><span></span></div>
  <h2>Little Rock's First and Only Specialized Arkansas Medical Network</h2>
  <p class="intro">We are the first clinic in the city dedicated only to medical cannabis care, with physicians who know state law.</p>
  <div class="fcard" style="left:148px"><div class="ph" role="img" aria-label="Close-up of green cannabis leaves"></div><h4>No Qualification? No Fee.</h4><p>If you do not qualify after your evaluation, you pay nothing.</p></div>
  <div class="fcard" style="left:456px"><div class="ph" role="img" aria-label="Cannabis leaves on a dark green background"></div><h4>No Qualification? No Fee.</h4><p>If you do not qualify after your evaluation, you pay nothing.</p></div>
  <div class="fcard" style="left:764px"><div class="ph" role="img" aria-label="Hand holding a cannabis leaf"></div><h4>No Qualification? No Fee.</h4><p>If you do not qualify after your evaluation, you pay nothing.</p></div>
</section>

<footer class="footer">
  <div class="brand"><i class="brand-mark"></i><span class="brand-name">Orlow Wellness Group</span></div>
  <p class="about">Caring physicians helping Arkansas patients find safe, legal relief.</p>
  <h4 style="left:412px">Quick Links</h4>
  <ul class="links"><li>Home</li><li>About</li><li>Qualify</li><li>Appointments</li><li>FAQ</li><li>News</li><li>Contact</li></ul>
  <h4 style="left:552px">Contact Us</h4>
  <ul class="clist">
    <li><svg width="16" height="20" viewBox="0 0 16 20" fill="#fff"><path d="M8 0a7 7 0 0 0-7 7c0 5 7 13 7 13s7-8 7-13a7 7 0 0 0-7-7zm0 10a3 3 0 1 1 0-6 3 3 0 0 1 0 6z"/></svg>123 Maple Row Little Rock</li>
    <li><svg width="18" height="14" viewBox="0 0 18 14" fill="none" stroke="#fff" stroke-width="2"><rect x="1" y="1" width="16" height="12"/><path d="M1 1l8 7 8-7"/></svg>care@orlowwellness.com</li>
    <li><svg width="16" height="16" viewBox="0 0 16 16" fill="#fff"><path d="M3 0l3 4-2 2c1 2 4 5 6 6l2-2 4 3-2 3C8 16 0 8 0 3z"/></svg>00-555-0142</li>
  </ul>
  <h4 style="left:784px">Get In Touch</h4>
  <div class="form">
    <div class="row"><span class="field">Name</span><span class="field">Email</span><span class="field">Phone</span></div>
    <div class="row"><span class="field msg">Message</span></div>
    <span class="btn">Subscribe</span>
  </div>
</footer>

<div class="copy">
  <p>Copyright © 2018 Orlow Wellness Group</p>
  <div class="social"><i class="dot"></i><i class="dot"></i><i class="dot"></i></div>
</div>

</body>
</html>
```